Professional University Report Template

I have the need for a professionally-designed, multi-page report template, consisting of 8.5 x 11 inch pages - like a book, but not facing page design. An InDesign template would be best for my purposes.

This is a professional document in which I will need a main column for text, and a side column (around 1/3 of the width) to include photos, graphics, quotes, and lists. No background colors should be used, but perhaps some shading would be fine. This will be distributed as a PDF and will be printed by many in greyscale - so it should look great, and be easy to view without color.

As it is for a university publication, it must be overall professional and a bit subdued. The design should not overshadow the content, but enhance the overall experience. Most of all, I am aiming for something that is original and interesting.

Target Market(s)

University professors

Industry/Entity Type

University

Requirements
Must have
• Title page

Then a 3-page example document (use the text from sample indicator doc file):
Header 1 text
Header 2 text
body text
bulleted list
footer text noting the chapter title and page number

In the side columns of example pages (use the image files):
Photos
graphs
quoted text
bulleted list
Should not have
• No need for table of contents page, logo placement, or headers

```html
<!DOCTYPE html>
<html lang="en">
<head>
<meta charset="utf-8">
<title>Department activity – page 3</title>
<link rel="stylesheet" href="https://fonts.googleapis.com/css2?family=Crimson+Text:ital,wght@0,400;0,600;0,700;1,700&display=swap">
<style>
  :root {
    --ink: #1c1c1c;
    --muted: #8a8a8a;
    --paper: #ffffff;
    --caption-band: #000000;
    --caption-text: #ffffff;
  }
  html, body {
    margin: 0;
    padding: 0;
    overflow: hidden;
    background: var(--paper);
  }
  .page {
    position: relative;
    width: 927px;
    height: 1200px;
    overflow: hidden;
    background: var(--paper);
    color: var(--ink);
    font-family: "Crimson Text", Georgia, serif;
  }
  .main-column {
    position: absolute;
    left: 82px;
    top: 49px;
    width: 504px;
    font-size: 14.6px;
    line-height: 19.9px;
  }
  .main-column p {
    margin: 0 0 18px;
    text-align: justify;
  }
  .main-column p.artifacts-heading {
    font-weight: 600;
    margin: 0 0 14px;
    text-align: left;
  }
  .artifact-list {
    list-style: none;
    margin: 0;
    padding: 0;
    width: 480px;
  }
  .artifact-list li {
    position: relative;
    padding-left: 17px;
    margin-bottom: 13px;
  }
  .artifact-list li::before {
    content: "";
    position: absolute;
    left: 7px;
    top: 9px;
    width: 4px;
    height: 4px;
    border-radius: 50%;
    background: var(--ink);
  }
  .side-column {
    position: absolute;
    left: 601px;
    top: 55px;
    width: 244px;
  }
  .photo-figure {
    position: absolute;
    left: 0;
    width: 244px;
    margin: 0;
  }
  .photo-figure .photo {
    display: block;
    width: 244px;
    height: 133px;
  }
  .photo-figure figcaption {
    height: 21px;
    background: var(--caption-band);
    color: var(--caption-text);
    font-style: italic;
    font-weight: 700;
    font-size: 11.5px;
    line-height: 21px;
    padding-left: 9px;
  }
  .figure-schoolhouse { top: 0; }
  .figure-classroom { top: 246px; }
  .figure-student { top: 477px; }
  .figure-schoolhouse .photo { background: linear-gradient(180deg, #6f7a5a 0%, #8f7a4e 45%, #a48a5a 70%, #9a8f6a 100%); }
  .figure-classroom .photo { background: linear-gradient(180deg, #7d6a4a 0%, #8a7a62 40%, #6f86a0 75%, #586a7a 100%); }
  .figure-student .photo { background: radial-gradient(ellipse at 50% 55%, #6a6050 0%, #3a342c 45%, #121212 80%); }
  .page-footer {
    position: absolute;
    top: 1128px;
    left: 0;
    width: 927px;
    text-align: center;
    font-size: 11.5px;
    line-height: 16px;
  }
  .page-number {
    color: var(--ink);
    padding-right: 6px;
    border-right: 1px solid var(--ink);
  }
  .chapter-title {
    color: var(--muted);
    padding-left: 6px;
  }
</style>
</head>
<body>
<div class="page">
  <main class="main-column">
    <p>This project allows groups of instructional technology students at Highland State University to collaborate online with peers associated with the agencies in southern India. During the course of the semester, my join class groups matched with providing a web design service to one of the NPO/NGOs in southern India that agreed to work together on this project.The student groups are required to communicate online throughout the semester with the agency and associates such as local teachers in the Tamil Nadu region of southern India.</p>
    <p>The task of my instructional technology students is to act as technology mentors to the agencies, with respect to communicating their message online through the agency website. This allows students to utilize web design skills developed in class, providing a connection of theory and practice that puts the course concepts into concrete form, and reciprocally benefits both the community agency and the students. Online communication tools are provided for students and their colleagues in India, and at points during the term all groups utilize a variety of asynchronous and synchronous e-learning communication tools.</p>
    <p class="artifacts-heading">Artifacts related to this indicator:</p>
    <ul class="artifact-list">
      <li>Highland &amp; the Community Together (HCT) Faculty Fellow 2009-2012 (announcement, application, and letter of award)</li>
      <li>College of Education Successful Adoption of Teaching Technology (SATT)<br>Grant (announcement, application, and letter of award)</li>
      <li>EDT 5410 syllabus reflecting service-learning project</li>
      <li>Summary of student feedback related to the service-learning project</li>
      <li>Poster presentation from the 2010 Society for Digital Learning and<br>Teacher Education (SDLTE) International Conference</li>
      <li>Homepage article on the Highland State University website related<br>to this course</li>
    </ul>
  </main>

  <aside class="side-column">
    <figure class="photo-figure figure-schoolhouse">
      <div class="photo" role="img" aria-label="Photo of a small rural schoolhouse under trees"></div>
      <figcaption>Lorem Ipsum</figcaption>
    </figure>
    <figure class="photo-figure figure-classroom">
      <div class="photo" role="img" aria-label="Photo of pupils in uniform seated in a classroom"></div>
      <figcaption>Lorem Ipsum</figcaption>
    </figure>
    <figure class="photo-figure figure-student">
      <div class="photo" role="img" aria-label="Video call still of a student standing in a classroom"></div>
      <figcaption>Lorem Ipsum</figcaption>
    </figure>
  </aside>

  <footer class="page-footer">
    <span class="page-number">3</span><span class="chapter-title">Department activity</span>
  </footer>
</div>
</body>
</html>
```